Está é a segunda experiência que tenho com site. Notei que na vês passada, comprando o mesmo pacotes, obtive no mínimo o dobro de projetos para escolher. Tento que para escolha de nome, não escolhi nenhum sugerido. São críticas, construtivas.

```html
<!DOCTYPE html>
<html lang="pt-BR">
<head>
<meta charset="UTF-8">
<title>Vitamed – Cartão de visita</title>
<link rel="stylesheet" href="https://fonts.googleapis.com/css2?family=Montserrat:wght@300;400;600&display=swap">
<style>
  :root {
    --teal: #2bb5ab;
    --teal-light: #8fd8d2;
    --white: #ffffff;
    --paper: #e9eaea;
    --ink-soft: #e6f7f5;
  }
  * { box-sizing: border-box; margin: 0; padding: 0; }
  html, body { width: 1200px; height: 1200px; overflow: hidden; }
  body {
    background: var(--paper);
    font-family: "Montserrat", Arial, sans-serif;
    display: flex; flex-direction: column; align-items: center; justify-content: center;
    gap: 60px;
  }
  .card {
    position: relative; width: 880px; height: 480px; overflow: hidden;
    box-shadow: 0 6px 18px rgba(0,0,0,0.12);
  }
  .brand-row { display: flex; align-items: center; }
  .brand-dot { border-radius: 50%; flex: none; }
  .brand-name { font-weight: 600; line-height: 1; letter-spacing: -1px; }
  .brand-tagline { font-weight: 300; white-space: nowrap; }

  /* Front */
  .card-front { background: var(--white); }
  .front-brand {
    position: absolute; left: 0; right: 0; top: 150px;
    display: flex; flex-direction: column; align-items: center;
  }
  .front-brand .brand-row { gap: 18px; }
  .front-brand .brand-dot { width: 34px; height: 34px; background: var(--teal); }
  .front-brand .brand-name { font-size: 76px; color: var(--teal); }
  .front-brand .brand-tagline { margin-top: 16px; font-size: 20px; letter-spacing: 8px; color: var(--teal-light); }
  .front-band { position: absolute; left: 0; bottom: 0; width: 100%; height: 16px; display: block; }

  /* Back */
  .card-back { background: var(--teal); color: var(--white); }
  .back-brand { position: absolute; left: 60px; top: 60px; }
  .back-brand .brand-row { gap: 12px; }
  .back-brand .brand-dot { width: 20px; height: 20px; background: var(--white); }
  .back-brand .brand-name { font-size: 44px; color: var(--white); }
  .back-brand .brand-tagline { margin-top: 10px; font-size: 11px; letter-spacing: 5px; color: var(--ink-soft); }
  .contact { position: absolute; left: 60px; top: 180px; font-size: 14px; line-height: 1.6; font-weight: 400; }
  .contact .role { font-weight: 300; font-size: 12px; opacity: .85; }
  .address {
    position: absolute; right: 60px; top: 250px; text-align: right;
    font-size: 12px; line-height: 1.7; font-weight: 300;
  }
</style>
</head>
<body>
  <section class="card card-front">
    <div class="front-brand">
      <div class="brand-row">
        <span class="brand-dot"></span>
        <span class="brand-name">Vitamed</span>
      </div>
      <div class="brand-tagline">CLÍNICA MÉDICA</div>
    </div>
    <svg class="front-band" viewBox="0 0 880 16" preserveAspectRatio="none">
      <rect x="0" y="6" width="880" height="10" fill="var(--teal)"/>
      <polygon points="600,16 640,6 880,6 880,16" fill="var(--teal-light)"/>
    </svg>
  </section>

  <section class="card card-back">
    <div class="back-brand">
      <div class="brand-row">
        <span class="brand-dot"></span>
        <span class="brand-name">Vitamed</span>
      </div>
      <div class="brand-tagline">CLÍNICA MÉDICA</div>
    </div>
    <div class="contact">
      <div>Nome Sobrenome</div>
      <div class="role">Cargo</div>
      <div>(71) 3000-0000</div>
      <div>contato@vitamedclinica.com.br</div>
    </div>
    <div class="address">
      <div>www.vitamedclinica.com.br</div>
      <div>Rua das Acácias, 120, Sala 4, Centro</div>
      <div>Salvador – BA, CEP 40000-000</div>
    </div>
  </section>
</body>
</html>
```